1 page A4 double sided Brochure Design Folded to envelope size. Interesting fold design would be co

Small family run guesthouse BnB in Blue Mountains Australia needs a new brochure showing different aspects of business

We need a new brochure to go with our new website. Basically the design would be good as a double sided brochure that can be folded down to standard envelope size.

We have seen a few interesting brochure designs before that fold in different ways (and therefore have the design to match) but still fold down to this size to help with postage.

The design would have to showcase the different aspects of our business including individual accommodation for couples and families, conference market, wedding market, retreat market and events market (parties, re-unions etc). The Business must be Showcased as The Fernhollow Lodge, Blue Mountains

It is possible to arrange design so folds separate different sections of info/pictures.

It is also optional that we possibly have 2 brochures instead, one that is a basic all inclusive once described and one that only deals with group bookings (wedding conference retreats etc etc)

Must match design elements from our web page. Feel free to take informations, elements and images from there for design www.fernhollowlodge.com.au

Here is a link to our view we wake up to every morning to inspire all those working on a design!
http://www.fernhollowlodge.com.au/images/view.jpg

Target Market(s)

Group bookings, weddings, conferences, retreats, events and Blue Mountains Travellers

Industry/Entity Type

Accommodation

Requirements
Must have
• Must be based on our current websites design feel, colours, etc
Must be showcased as The Fernhollow Lodge Blue Mountains.
Must mention The Blue Mountains as a world heritage destination
Must be A4 double sided that can fold down to 1/3 the size to fit into a standard envelope. Any designs that will not fit in a standard envelope once folded can not be accepted as they are outside the brief
Nice to have
• Interesting folding design to get people interested to read it.

```html
<!DOCTYPE html>
<html lang="en">
<head>
<meta charset="utf-8">
<title>The Fernhollow Lodge – Events Brochure</title>
<link rel="stylesheet" href="https://fonts.googleapis.com/css2?family=Jost:wght@400;600&family=Exo+2:ital,wght@1,400&family=EB+Garamond:ital@0;1&family=Arimo&display=swap">
<style>
  :root {
    --ink: #000000;
    --paper: #ffffff;
    --gold: #c9a77a;
    --gold-soft: #d8c3a0;
    --rule: #5a5a5a;
    --bar-top: #8a8a8a;
    --bar-bottom: #1c1c1c;
  }
  * { box-sizing: border-box; margin: 0; padding: 0; }
  html, body { width: 875px; height: 1200px; overflow: hidden; background: var(--ink); }
  .brochure { position: relative; width: 875px; height: 1200px; background: var(--ink); color: var(--paper); font-family: "Jost", sans-serif; }
  .abs { position: absolute; }
  .panel { position: absolute; left: 0; width: 875px; }
  .panel--events { top: 0; height: 400px; }
  .panel--contact { top: 400px; height: 400px; transform: rotate(180deg); }
  .panel--cover { top: 800px; height: 400px; }
  .divider { position: absolute; left: 0; width: 875px; height: 1px; background: var(--rule); }

  .swirl-band { background: linear-gradient(90deg, rgba(58,52,52,0.25), rgba(70,64,62,0.55), rgba(58,52,52,0.25)); border-radius: 30px; }

  .events-title { left: 39px; top: 78px; font-weight: 600; font-size: 21px; line-height: 26px; color: var(--gold); letter-spacing: 0.5px; }
  .events-copy { left: 39px; top: 110px; width: 412px; font-size: 11.2px; line-height: 13.6px; text-align: justify; }
  .events-copy p { margin-bottom: 13.6px; }

  .photo { position: absolute; }
  .photo--lawn { background: linear-gradient(180deg, #7fa7d8 0%, #a7c0dc 40%, #3b4a2e 60%, #d9d9dc 100%); }
  .photo--table { background: linear-gradient(160deg, #5c7482 0%, #e8e6e0 45%, #f3f1ec 70%, #d76a2a 100%); }
  .photo--harp { background: linear-gradient(180deg, #f0f0f0 0%, #3f5a2c 45%, #b23a38 75%, #5a3a24 100%); }
  .photo--lollies { background: linear-gradient(180deg, #c8b1d8 0%, #eee7ee 40%, #b7554b 100%); }
  .photo--balloons { background: linear-gradient(180deg, #b8361f 0%, #c44a2e 60%, #e8e2d6 100%); }
  .photo--marquee { background: linear-gradient(180deg, #5d7e9c 0%, #eeeeee 35%, #2a2a2a 70%, #c33 100%); }
  .photo--valley { background: linear-gradient(180deg, #7f8e86 0%, #c9c7b8 40%, #2e3a22 100%); }
  .photo--room { background: linear-gradient(135deg, #c9c4a8 0%, #e6ddd0 40%, #a8432e 70%, #d9d4c7 100%); }
  .photo--dinner { background: linear-gradient(180deg, #6c8fbf 0%, #2f3a24 45%, #111 70%, #c22525 100%); }
  .photo--pool { background: linear-gradient(180deg, #2f64b8 0%, #7aa3d6 45%, #1f2a1b 65%, #45c1c9 100%); }

  .contact-lines { left: 550px; top: 175px; width: 250px; font-weight: 600; font-size: 15px; line-height: 21px; color: var(--gold-soft); }
  .contact-lines .phone { font-size: 19px; line-height: 26px; }

  .brand-name { font-family: "Jost", sans-serif; font-weight: 400; color: var(--gold); white-space: nowrap; }

  .tagline { left: 178px; top: 45px; width: 665px; font-family: "Exo 2", sans-serif; font-style: italic; font-size: 15.5px; line-height: 20px; color: var(--gold); text-align: center; }

  .nav-bar { left: 0; top: 101px; width: 875px; height: 34px; background: linear-gradient(180deg, var(--bar-top) 0%, #4a4a4a 45%, var(--bar-bottom) 100%); display: flex; align-items: center; justify-content: flex-end; padding-right: 38px; font-family: "Arimo", sans-serif; font-size: 14.5px; color: var(--paper); }
  .nav-item { display: flex; align-items: center; }
  .nav-sep { width: 6px; height: 6px; border-radius: 50%; background: #cfcfcf; margin: 0 14px; }

  .footer-contact { left: 39px; top: 322px; font-family: "Arimo", sans-serif; font-size: 11px; line-height: 14px; }
  .footer-line { font-family: "EB Garamond", serif; font-style: italic; font-size: 15px; line-height: 18px; color: var(--paper); }
</style>
</head>
<body>
<main class="brochure">

  <section class="panel panel--events">
    <div class="abs swirl-band" style="left:10px;top:2px;width:850px;height:70px" role="img" aria-label="Decorative swirling flourish border"></div>
    <h1 class="abs events-title">EVENTS</h1>
    <div class="abs events-copy">
      <p>Reunions, birthdays, church groups, parties, family get togethers and more The Fernhollow Lodge Blue Mountains is the perfect function venue to get together and really leave the world behind whilst re-connecting with your friends and family.</p>
      <p>Specializing in group bookings our flexibility can help tailor a package to really fit in with your exact vision for your special event. Being a very private, flexible venue on 32 acres backing onto national park land allows us to really open up your options when planning your function and with many of our friendly staff living on site your guests will quickly feel more at home than you could imagine possible.</p>
      <p>At The Fernhollow Lodge we can cater for any type of function or event or recommend the perfect caterer to suit your needs and budget. We are also fully licensed with Australian beer on tap and an excellent selection of local wines so can cover all your beverage needs as well.</p>
      <p>Once you take The Fernhollow Lodge exclusively it becomes your own private haven from the rest of civilization to really break free and re-establish the truely important things.</p>
    </div>
    <div class="photo photo--lawn" style="left:464px;top:115px;width:186px;height:240px" role="img" aria-label="Outdoor lawn set with white-covered chairs under umbrellas and blue sky"></div>
    <div class="photo photo--table" style="left:660px;top:115px;width:185px;height:240px" role="img" aria-label="Table setting with glasses and an orange lily centrepiece"></div>
  </section>

  <div class="divider" style="top:400px"></div>

  <section class="panel panel--contact">
    <div class="photo photo--harp" style="left:285px;top:198px;width:237px;height:172px" role="img" aria-label="Harpist playing in a garden"></div>
    <div class="photo photo--lollies" style="left:33px;top:198px;width:236px;height:172px" role="img" aria-label="Lolly jars on a decorated dessert table"></div>
    <div class="photo photo--balloons" style="left:285px;top:31px;width:237px;height:153px" role="img" aria-label="Balloons hanging from a ceiling light in a red room"></div>
    <div class="photo photo--marquee" style="left:33px;top:31px;width:236px;height:153px" role="img" aria-label="Outdoor party tables with umbrellas"></div>
    <div class="abs swirl-band" style="left:550px;top:305px;width:286px;height:65px" role="img" aria-label="Decorative swirling flourish"></div>
    <div class="abs contact-lines">
      <div class="phone">02 4700 5318</div>
      <div>info@fernhollowlodge.com.au</div>
      <div>info@ridgelinemail.com.au</div>
      <div>www.fernhollowlodge.com.au</div>
    </div>
    <p class="abs brand-name" style="left:552px;top:80px;font-size:17px">The Fernhollow</p>
  </section>

  <div class="divider" style="top:799px"></div>

  <section class="panel panel--cover">
    <p class="abs brand-name" style="left:39px;top:62px;font-size:17px">The Fernhollow</p>
    <p class="abs tagline">Family owned and run Blue Mountains accommodation, retreat, conference, wedding and function centre set on 32 acres of virgin bushland in the beauty of a world heritage location.</p>
    <nav class="abs nav-bar">
      <span class="nav-item">Accommodation</span><span class="nav-sep"></span>
      <span class="nav-item">Conference</span><span class="nav-sep"></span>
      <span class="nav-item">Weddings</span><span class="nav-sep"></span>
      <span class="nav-item">Functions</span><span class="nav-sep"></span>
      <span class="nav-item">Group Stays</span><span class="nav-sep"></span>
      <span class="nav-item">Retreats</span>
    </nav>
    <div class="photo photo--valley" style="left:0;top:139px;width:198px;height:151px" role="img" aria-label="Misty morning view over the bushland valley"></div>
    <div class="photo photo--room" style="left:201px;top:139px;width:234px;height:151px" role="img" aria-label="Guest bedroom with French doors and red curtains"></div>
    <div class="photo photo--dinner" style="left:438px;top:139px;width:236px;height:151px" role="img" aria-label="Outdoor dinner table with red napkins and wine glasses"></div>
    <div class="photo photo--pool" style="left:677px;top:139px;width:198px;height:151px" role="img" aria-label="Swimming pool with umbrellas and bush view"></div>
    <div class="abs swirl-band" style="left:10px;top:322px;width:855px;height:74px" role="img" aria-label="Decorative swirling flourish border"></div>
    <div class="abs footer-contact">
      <div>02 4700 5318</div>
      <div>info@fernhollowlodge.com.au</div>
      <div>www.fernhollowlodge.com.au</div>
    </div>
    <p class="abs footer-line" style="left:345px;top:320px">Individual accommodation or Group stays</p>
    <p class="abs footer-line" style="left:632px;top:340px">So close by ... but worlds away</p>
  </section>

</main>
</body>
</html>
```